Homepage/Landing Page for Kelvadu.com

We need a brochure style landing page for our website, kelvadu.com. The new homepage will direct people either to trademarkhub.com (a website for businesses to purchase printing), to a landing page about trading cards/sports memorabilia, or to a website about high-end embellished cartons/boxes.
The existing site, www.kelvadu.com, will become trademarkhub.com, and people arriving at kelvadu.com will be shown three options to choose based on their needs:
1) Business Printing - for everyone from micro-businesses on up, our manufacturing process insures we have something to suit every business.
2) Highly decorated and embellished cartons - perfect for new brands, prototypes, pilot programs, seasonal packaging
3) Trading cards/sports memorabilia - Handling cards for athletes from Tidy Circuit to high school, college and beyond.

Target Market(s)

Target market is small business owners and print buyers

Industry/Entity Type

Printing and Packaging

Number of Pages Required

1 page

Font styles to use
Other font styles liked:
• See the KV Web Flip Standards PDF attached.

Requirements
Must have
• 3 clearly marked paths for customers to follow - use web standards pdf below for fonts and colors
Should not have
• My project should not feel trendy or faddish, but modern and professional.

```html
<!DOCTYPE html>
<html lang="en">
<head>
<meta charset="utf-8">
<title>Kelvadu – Positively Different</title>
<link rel="stylesheet" href="https://fonts.googleapis.com/css2?family=Roboto:wght@300;400;700;900&family=Roboto+Slab:wght@400;800&display=swap">
<style>
  :root {
    --teal: #0aa9c8;
    --teal-deep: #0794b3;
    --teal-soft: #3cc0da;
    --white: #ffffff;
    --ink: #111111;
    --footer: #050505;
    --stage: #f1f1f1;
    --icon-blue: #1ba8cc;
  }
  * { box-sizing: border-box; margin: 0; padding: 0; }
  html, body { width: 1038px; height: 1200px; overflow: hidden; }
  body { background: var(--stage); position: relative; font-family: "Roboto", sans-serif; }

  .landing {
    position: absolute; left: 0; top: 308px;
    width: 1038px; height: 584px; overflow: hidden;
    background: var(--teal);
  }
  .hero-backdrop {
    position: absolute; inset: 0 0 46px 0;
    background:
      radial-gradient(ellipse 260px 220px at 660px 140px, rgba(120,215,235,0.45), transparent 70%),
      radial-gradient(ellipse 300px 260px at 880px 210px, rgba(0,110,140,0.35), transparent 70%),
      radial-gradient(ellipse 280px 240px at 160px 420px, rgba(0,120,150,0.3), transparent 70%),
      linear-gradient(160deg, var(--teal-soft) 0%, var(--teal) 45%, var(--teal-deep) 100%);
  }

  .brand {
    position: absolute; left: 0; right: 0; top: 24px;
    display: flex; flex-direction: column; align-items: center; gap: 8px;
    color: var(--white);
  }
  .brand-mark {
    width: 54px; height: 54px; border-radius: 50%;
    border: 3px solid var(--white);
  }
  .brand-name {
    font-family: "Roboto", sans-serif; font-weight: 300;
    font-size: 30px; line-height: 1; letter-spacing: 0.5px;
  }

  .headline {
    position: absolute; left: 0; right: 0; top: 158px;
    text-align: center; color: var(--white);
    font-family: "Roboto Slab", serif; font-weight: 800;
    font-size: 43px; letter-spacing: 2.5px; line-height: 1;
  }

  .paths {
    position: absolute; left: 114px; top: 257px;
    display: flex; gap: 18px;
  }
  .path-card {
    position: relative; width: 258px; height: 254px;
    border: 2px solid var(--white); border-radius: 12px;
    background: transparent;
    display: flex; flex-direction: column; align-items: center;
  }
  .path-icon {
    position: absolute; top: -31px; left: 50%; transform: translateX(-50%);
    width: 58px; height: 58px; border-radius: 50%;
    background: var(--white);
    display: flex; align-items: flex-start; justify-content: center; padding-top: 8px;
  }
  .path-head {
    width: 100%; height: 59px; background: var(--white);
    border-radius: 10px 10px 0 0;
    display: flex; align-items: flex-end; justify-content: center;
    padding-bottom: 8px;
  }
  .path-title {
    font-weight: 700; font-size: 12.5px; line-height: 16px;
    text-align: center; color: var(--ink); letter-spacing: 0.3px;
    position: relative; z-index: 1;
  }
  .path-photo {
    width: 244px; height: 96px; margin-top: 4px;
    border: 2px solid var(--white);
  }
  .photo-press { background: linear-gradient(100deg, #2a2d33 0%, #474b52 35%, #c98a2a 60%, #e1531c 75%, #2b5fa8 100%); }
  .photo-carton { background: linear-gradient(100deg, #b9a5d6 0%, #d8bd98 35%, #cfae86 60%, #e9e4ee 85%, #bda6d8 100%); }
  .photo-cards { background: linear-gradient(100deg, #f3f3f5 0%, #2f4f9e 30%, #e2c23b 55%, #2b8a6b 75%, #c43c2c 100%); }
  .path-text {
    margin-top: 10px; padding: 0 10px;
    font-family: "Roboto Slab", serif; font-weight: 400;
    font-size: 10px; line-height: 15px; text-align: center; color: var(--white);
  }
  .read-more {
    position: absolute; bottom: 12px; left: 50%; transform: translateX(-50%);
    height: 20px; padding: 0 8px 0 10px; border-radius: 10px;
    background: var(--ink); color: var(--white);
    font-weight: 700; font-size: 9px; text-decoration: none;
    display: flex; align-items: center; gap: 6px; white-space: nowrap;
  }

  .site-footer {
    position: absolute; left: 0; right: 0; bottom: 0; height: 46px;
    background: var(--footer); color: var(--white);
    display: flex; align-items: center; justify-content: space-between;
    padding: 0 114px;
  }
  .copyright { font-size: 12px; letter-spacing: 0.3px; }
  .follow { display: flex; align-items: center; gap: 8px; }
  .follow-label { font-weight: 700; font-size: 12px; margin-right: 8px; }
  .social-dot {
    width: 21px; height: 21px; border-radius: 50%;
    background: var(--icon-blue);
  }
</style>
</head>
<body>
  <main class="landing">
    <div class="hero-backdrop" role="img" aria-label="Photo of smiling print shop staff at work, under a teal colour overlay"></div>

    <div class="brand">
      <div class="brand-mark"></div>
      <div class="brand-name">kelvadu</div>
    </div>

    <h1 class="headline">POSITIVELY DIFFERENT.</h1>

    <section class="paths">
      <article class="path-card">
        <div class="path-icon">
          <svg width="24" height="26" viewBox="0 0 24 26" fill="none" stroke="var(--icon-blue)" stroke-width="1.4">
            <rect x="6" y="1" width="12" height="8" rx="1"/>
            <rect x="1.5" y="9" width="21" height="10" rx="2"/>
            <rect x="5" y="15" width="14" height="10" rx="1"/>
            <line x1="8" y1="19" x2="16" y2="19"/>
            <line x1="8" y1="22" x2="14" y2="22"/>
            <circle cx="19" cy="12.5" r="0.9"/>
          </svg>
        </div>
        <div class="path-head"><h2 class="path-title">BUSINESS<br>PRINTING</h2></div>
        <div class="path-photo photo-press" role="img" aria-label="Photo of a large-format printer producing a colourful print"></div>
        <p class="path-text">for everyone from micro-businesses on up, our manufacturing process insures we have something to suit every business.</p>
        <a class="read-more" href="#">Read More
          <svg width="10" height="10" viewBox="0 0 10 10" fill="none" stroke="#fff" stroke-width="1"><circle cx="5" cy="5" r="4.3"/><path d="M3 5h4M5.3 3.3 7 5 5.3 6.7"/></svg>
        </a>
      </article>

      <article class="path-card">
        <div class="path-icon">
          <svg width="30" height="26" viewBox="0 0 30 26" fill="none" stroke="var(--icon-blue)" stroke-width="1.4">
            <rect x="10" y="1" width="11" height="9" rx="1"/>
            <rect x="2" y="10" width="12" height="10" rx="1"/>
            <rect x="15" y="8" width="13" height="12" rx="1"/>
            <rect x="8" y="17" width="12" height="8" rx="1"/>
            <line x1="15.5" y1="1" x2="15.5" y2="5"/>
            <line x1="21.5" y1="8" x2="21.5" y2="12"/>
          </svg>
        </div>
        <div class="path-head"><h2 class="path-title">HIGHLY DECORATED AND<br>EMBELLISHED CARTONS</h2></div>
        <div class="path-photo photo-carton" role="img" aria-label="Photo of kraft gift boxes tied with string among lilac flowers"></div>
        <p class="path-text">perfect for new brands, prototypes,<br>pilot programs, seasonal<br>packaging</p>
        <a class="read-more" href="#">Read More
          <svg width="10" height="10" viewBox="0 0 10 10" fill="none" stroke="#fff" stroke-width="1"><circle cx="5" cy="5" r="4.3"/><path d="M3 5h4M5.3 3.3 7 5 5.3 6.7"/></svg>
        </a>
      </article>

      <article class="path-card">
        <div class="path-icon">
          <svg width="22" height="27" viewBox="0 0 22 27" fill="none" stroke="var(--icon-blue)" stroke-width="1.4">
            <rect x="5" y="4" width="15" height="21" rx="2"/>
            <rect x="2" y="1.5" width="15" height="21" rx="2" fill="#fff"/>
            <circle cx="9.5" cy="10" r="4"/>
            <line x1="5" y1="18" x2="14" y2="18"/>
          </svg>
        </div>
        <div class="path-head"><h2 class="path-title">TRADING CARDS/SPORTS<br>MEMORABILIA</h2></div>
        <div class="path-photo photo-cards" role="img" aria-label="Photo of a pile of colourful collectible trading cards"></div>
        <p class="path-text">Handling cards for athletes from Tidy Circuit<br>to high school, college<br>and beyond.</p>
        <a class="read-more" href="#">Read More
          <svg width="10" height="10" viewBox="0 0 10 10" fill="none" stroke="#fff" stroke-width="1"><circle cx="5" cy="5" r="4.3"/><path d="M3 5h4M5.3 3.3 7 5 5.3 6.7"/></svg>
        </a>
      </article>
    </section>

    <footer class="site-footer">
      <p class="copyright">COPYRIGHT &nbsp;@ 2022 KELVADU, ALL RIGHT RESERVED.</p>
      <div class="follow">
        <span class="follow-label">Follow us on</span>
        <span class="social-dot"></span>
        <span class="social-dot"></span>
        <span class="social-dot"></span>
        <span class="social-dot"></span>
      </div>
    </footer>
  </main>
</body>
</html>
```